RevelHubQZ Business Cards

Front
Has logo with a design. Website address (www.revelhubqz.example)
Has slogan (discover nightlife)
Has phone number (5129873304)
Should be bold and stands out.

Back
Has details about what we offer.

Events
Search upcoming events
Submit events
Party Image Gallery
View and download HQ party images
Sign up as a contributing event photographer and get paid!
Tickets
Sell your event tickets online for free!
Direct pay
No ticket fee

Target Market(s)

These cards will be handed out in clubs and events to patrons.

Industry/Entity Type

Business

Contact Information for Business Card

Should match or mirror our website in some sort of way. Visit the website to get ideas.

Requirements
Must have
• Must be designed for a 3x3 inch card.

```html
<!DOCTYPE html>
<html lang="en">
<head>
<meta charset="utf-8">
<title>RevelHubQZ Business Cards</title>
<link href="https://fonts.googleapis.com/css2?family=Questrial&family=Montserrat:wght@600&family=Oswald:wght@400;600&display=swap" rel="stylesheet">
<style>
  :root {
    --stage: #e0e0de;
    --card: #fafafa;
    --blue: #1bb0e6;
    --pink: #e2388d;
    --ink: #2b2b2b;
    --muted: #555555;
  }
  * { box-sizing: border-box; margin: 0; padding: 0; }
  html, body { width: 1200px; height: 659px; overflow: hidden; background: var(--stage); }
  .card {
    position: absolute; top: 142px; width: 374px; height: 374px;
    background: var(--card); overflow: hidden;
  }
  .card--front { left: 201px; }
  .card--back { left: 624px; }

  .brand { position: absolute; left: 27px; top: 50px; display: flex; align-items: center; gap: 10px; }
  .brand__dot { width: 44px; height: 44px; border-radius: 50%; background: var(--blue); }
  .brand__name { font-family: "Questrial", sans-serif; font-size: 32px; color: var(--blue); line-height: 1; }
  .brand__tagline {
    position: absolute; left: 97px; top: 90px;
    font-family: "Questrial", sans-serif; font-size: 10px; letter-spacing: 5.6px; color: var(--muted);
  }

  .person { position: absolute; left: 27px; top: 194px; }
  .person__name { font-family: "Montserrat", sans-serif; font-weight: 600; font-size: 20px; color: var(--ink); }
  .person__role { font-family: "Questrial", sans-serif; font-size: 12px; color: var(--muted); margin-top: 2px; }
  .contact { position: absolute; left: 27px; top: 255px; font-family: "Questrial", sans-serif; font-size: 14px; color: var(--ink); line-height: 18.5px; }
  .contact .accent { color: var(--blue); }
  .contact .accent-pink { color: var(--pink); }

  .eq-band { position: absolute; left: 0; bottom: 0; width: 100%; height: 32px;
    background: linear-gradient(to bottom, var(--pink) 0%, var(--pink) 30%, var(--blue) 55%, var(--blue) 100%); opacity: .9; }

  .offer__title { position: absolute; left: 30px; top: 40px; font-family: "Oswald", sans-serif; font-weight: 600; font-size: 17px; color: var(--pink); letter-spacing: .5px; }
  .offer__list { position: absolute; left: 30px; top: 75px; list-style: none; font-family: "Oswald", sans-serif; font-size: 14.5px; color: var(--ink); }
  .offer__list li { height: 21.8px; line-height: 21.8px; }
  .offer__list li::before { content: "»"; display: inline-block; width: 13px; }

  .side-brand {
    position: absolute; left: 310px; top: 256px; width: 224px;
    transform: rotate(-90deg); transform-origin: 0 0;
    white-space: nowrap;
  }
  .side-brand__name { display: block; font-family: "Questrial", sans-serif; font-size: 30px; color: var(--blue); line-height: 30px; }
  .side-brand__tagline { display: block; margin-top: 3px; font-family: "Questrial", sans-serif; font-size: 9px; line-height: 10px; letter-spacing: 6.4px; color: var(--muted); }
  .side-brand__dot { position: absolute; left: 302px; top: 270px; width: 42px; height: 42px; border-radius: 50%; background: var(--blue); }
</style>
</head>
<body>
  <section class="card card--front">
    <div class="brand">
      <span class="brand__dot"></span>
      <span class="brand__name">RevelHubQZ</span>
    </div>
    <p class="brand__tagline">discover nightlife</p>

    <div class="person">
      <p class="person__name">Dana Whitlow</p>
      <p class="person__role">Managing Director</p>
    </div>
    <p class="contact">
      5129873304<br>
      support@revelhubqz.example<br>
      www.<span class="accent">revelhub</span><span class="accent-pink">qz</span>.example
    </p>
    <div class="eq-band" role="img" aria-label="Pink and blue equalizer bar pattern"></div>
  </section>

  <section class="card card--back">
    <h2 class="offer__title">WE OFFER</h2>
    <ul class="offer__list">
      <li>Events</li>
      <li>Search upcoming events</li>
      <li>Submit events</li>
      <li>Party Image Gallery</li>
      <li>View and download HQ party images</li>
      <li>Sign up as a contributing event</li>
      <li>photographer and get paid!</li>
      <li>Tickets</li>
      <li>Sell your event tickets online for free!</li>
      <li>Direct pay</li>
      <li>No ticket fee</li>
    </ul>
    <div class="side-brand">
      <span class="side-brand__name">RevelHubQZ</span>
      <span class="side-brand__tagline">discover nightlife</span>
    </div>
    <span class="side-brand__dot"></span>
    <div class="eq-band" role="img" aria-label="Pink and blue equalizer bar pattern"></div>
  </section>
</body>
</html>
```